BrivoLane Ute.

I want the full logo on one side. And the other side the card if right Ralf the logo the left half orange like the car in the logo color with Danielle R Morrow
Founder and CEO
Email symbol then dmorrow@brivolaneute.com
Www symbol. Then Brivolaneute.com
Phone symbol then 413-926-BRIV
The very bottom would like Brivo Lane Ute is a division of Harmond Vistas. LLC

```html
<!DOCTYPE html>
<html lang="en">
<head>
<meta charset="UTF-8">
<title>Brivo Lane Ute — Business Card</title>
<link href="https://fonts.googleapis.com/css2?family=Raleway:wght@300;400;700&family=Open+Sans:wght@400&display=swap" rel="stylesheet">
<style>
  :root {
    --backdrop: #dcdcdc;
    --card-white: #f7f7f7;
    --brand-orange: #e88a23;
    --ink: #1c1c1c;
    --on-orange: #ffffff;
    --shadow: rgba(0, 0, 0, 0.28);
  }
  * { margin: 0; padding: 0; box-sizing: border-box; }
  html, body {
    width: 1200px;
    height: 900px;
    overflow: hidden;
    background: var(--backdrop);
  }
  .canvas {
    position: relative;
    width: 1200px;
    height: 900px;
  }
  .card {
    position: absolute;
    width: 600px;
    height: 343px;
    border-radius: 26px;
    background: var(--card-white);
    box-shadow: 0 4px 0 #c9c9c9, 0 8px 0 #bdbdbd, 0 18px 30px var(--shadow);
    overflow: hidden;
  }

  /* Front: logo side */
  .card--front {
    left: 520px;
    top: 90px;
    display: flex;
    align-items: center;
    justify-content: center;
  }
  .brand-lockup {
    display: flex;
    flex-direction: column;
    align-items: center;
    gap: 14px;
  }
  .brand-lockup__art {
    width: 230px;
    height: 110px;
    border-radius: 10px;
    background: linear-gradient(135deg, #f3b566 0%, var(--brand-orange) 55%, #9fd6c8 100%);
  }
  .brand-lockup__name {
    font-family: "Raleway", sans-serif;
    font-weight: 700;
    font-size: 40px;
    letter-spacing: 1px;
    color: var(--ink);
    text-transform: uppercase;
  }

  /* Back: contact side */
  .card--back {
    left: 80px;
    top: 470px;
    display: flex;
  }
  .contact-panel {
    width: 46%;
    height: 100%;
    background: var(--brand-orange);
    color: var(--on-orange);
    padding: 34px 0 0 32px;
    font-family: "Raleway", sans-serif;
  }
  .contact-panel__name {
    font-size: 21px;
    font-weight: 300;
    letter-spacing: -0.3px;
    text-transform: uppercase;
  }
  .contact-panel__name strong { font-weight: 700; }
  .contact-panel__role {
    font-size: 17px;
    font-weight: 300;
    margin-top: 4px;
  }
  .contact-list {
    list-style: none;
    margin-top: 96px;
    display: flex;
    flex-direction: column;
    gap: 11px;
  }
  .contact-list__item {
    display: flex;
    align-items: center;
    gap: 9px;
    font-size: 15px;
    font-weight: 300;
  }
  .contact-list__icon { width: 18px; height: 18px; flex: none; }

  .logo-panel {
    position: relative;
    flex: 1;
    height: 100%;
  }
  .logo-panel__lockup {
    position: absolute;
    left: 38%;
    top: 50%;
    transform: translate(-50%, -50%) rotate(-90deg);
    display: flex;
    flex-direction: column;
    align-items: center;
    gap: 10px;
  }
  .logo-panel__art {
    width: 170px;
    height: 80px;
    border-radius: 8px;
    background: linear-gradient(135deg, #f3b566 0%, var(--brand-orange) 55%, #9fd6c8 100%);
  }
  .logo-panel__name {
    font-family: "Raleway", sans-serif;
    font-weight: 700;
    font-size: 28px;
    color: var(--ink);
    text-transform: uppercase;
    white-space: nowrap;
  }
  .division-note {
    position: absolute;
    right: -130px;
    top: 50%;
    transform: translateY(-50%) rotate(-90deg);
    width: 300px;
    text-align: center;
    font-family: "Open Sans", sans-serif;
    font-size: 13px;
    color: var(--ink);
    white-space: nowrap;
  }
</style>
</head>
<body>
<main class="canvas">

  <section class="card card--front" aria-label="Card front">
    <div class="brand-lockup">
      <div class="brand-lockup__art" role="img" aria-label="Illustration of an orange station wagon with surfboard, fence and sun"></div>
      <div class="brand-lockup__name">Brivo Lane Ute</div>
    </div>
  </section>

  <section class="card card--back" aria-label="Card back">
    <div class="contact-panel">
      <h1 class="contact-panel__name">Danielle R <strong>Morrow</strong></h1>
      <p class="contact-panel__role">Founder and CEO</p>
      <ul class="contact-list">
        <li class="contact-list__item">
          <svg class="contact-list__icon" viewBox="0 0 24 24" fill="none" stroke="currentColor" stroke-width="1.8" stroke-linejoin="round"><path d="M5 3h4l2 5-2.5 1.5a11 11 0 0 0 6 6L16 13l5 2v4a2 2 0 0 1-2 2A16 16 0 0 1 3 5a2 2 0 0 1 2-2z"/></svg>
          <span>413-926-BRIV</span>
        </li>
        <li class="contact-list__item">
          <svg class="contact-list__icon" viewBox="0 0 24 24" fill="none" stroke="currentColor" stroke-width="1.8" stroke-linejoin="round"><rect x="3" y="5" width="18" height="14" rx="1"/><path d="M3 6l9 7 9-7"/></svg>
          <span>dmorrow@brivolaneute.com</span>
        </li>
        <li class="contact-list__item">
          <svg class="contact-list__icon" viewBox="0 0 24 24" fill="none" stroke="currentColor" stroke-width="1.6"><circle cx="12" cy="12" r="9"/><ellipse cx="12" cy="12" rx="4" ry="9"/><path d="M3 12h18"/></svg>
          <span>www.Brivolaneute.com</span>
        </li>
      </ul>
    </div>
    <div class="logo-panel">
      <div class="logo-panel__lockup">
        <div class="logo-panel__art" role="img" aria-label="Illustration of an orange station wagon with surfboard, fence and sun"></div>
        <div class="logo-panel__name">Brivo Lane Ute</div>
      </div>
      <p class="division-note">Brivo Lane Ute is a division of Harmond Vistas. LLC</p>
    </div>
  </section>

</main>
</body>
</html>
```